Design graphics and Print for a line of Herb Seeds- Envelope Design

We need a set of herb seed envelopes designed for a new seed line we are launching.
The design will be both front and back

Envelope will be a colored ( green) ) envelope with white text
or a white or cream envelope in all black /and images text. Or can add some colors to the white envelope.

I have attached the die-cut of the seed envelope.
I have attached some images of envelopes I like. Please do not copy, these are just to give you an idea of what I like.

Please feel free to reach out to me if you have any questions.

Thank you

Target Market(s)

The design needs to classic that can translate to 3 different audiences. 1. young parents 2. hip, young single millennial 3. kids

Industry/Entity Type

Ecommerce

Font styles to use
Serif

Requirements
Must have
• Please use the herb - Parsley for the design
Icon, Text or both.

Front side must have:
1.either herb Icon or work Parsley or both- this will be the main attraction
2. company name- Tall Meadow Pantry
3. can use design elements
4. can use my logo on from or back or not at all. I

Backside must have:
1. social media tags
FB, Instagram and Pinterest ( use icons) @tallmeadowpantry

my website: www.tallmeadowpantry.example
this can be on from or back of the envelope.
Should not have
• please stay away from "county" flowery, old fashioned style designs

```html
<!DOCTYPE html>
<html lang="en">
<head>
<meta charset="utf-8">
<title>Tall Meadow Pantry – Parsley Seed Envelope</title>
<link rel="stylesheet" href="https://fonts.googleapis.com/css2?family=Tinos:wght@400;700&family=Arimo:wght@400;700&display=swap">
<style>
  :root {
    --stage: #666666;
    --leaf: #5fab2a;
    --leaf-deep: #4f9225;
    --ink: #3f3226;
    --paper: #ffffff;
    --herb-light: #8fd04e;
    --herb-dark: #3d8a1c;
  }
  html, body {
    margin: 0;
    padding: 0;
    overflow: hidden;
    background: var(--stage);
  }
  .canvas {
    position: relative;
    width: 1200px;
    height: 885px;
    background: var(--stage);
    overflow: hidden;
  }
  .dieline {
    position: absolute;
    inset: 0;
  }
  .label {
    position: absolute;
    color: var(--paper);
    white-space: nowrap;
    margin: 0;
  }
  .back-text {
    left: 260px;
    width: 291px;
    text-align: center;
    font-family: "Arimo", Arial, sans-serif;
  }
  .seal-name {
    position: absolute;
    left: 333px;
    top: 277px;
    width: 146px;
    height: 146px;
    display: flex;
    align-items: center;
    justify-content: center;
    text-align: center;
    font-family: "Tinos", "Times New Roman", serif;
    font-size: 19px;
    line-height: 1.2;
    letter-spacing: 2px;
    color: var(--ink);
  }
  .kicker { top: 452px; font-size: 15px; letter-spacing: 0.3px; }
  .product { top: 470px; font-size: 22px; font-weight: 700; letter-spacing: 0.8px; }
  .website { top: 526px; font-size: 14px; }
  .handle { top: 602px; font-size: 12px; }
  .brand-title {
    left: 579px;
    width: 348px;
    top: 462px;
    text-align: center;
    font-family: "Tinos", "Times New Roman", serif;
    font-size: 44px;
    line-height: 47px;
    letter-spacing: 0.5px;
  }
  .front-foot {
    top: 648px;
    font-family: "Arimo", Arial, sans-serif;
    font-weight: 700;
    font-size: 17px;
  }
  .seed-name { left: 598px; }
  .net-weight { right: calc(1200px - 909px); top: 651px; }
</style>
</head>
<body>
<main class="canvas">
  <svg class="dieline" width="1200" height="885" viewBox="0 0 1200 885" xmlns="http://www.w3.org/2000/svg">
    <defs>
      <radialGradient id="herbGlow" cx="0.5" cy="0.55" r="0.5">
        <stop offset="0" stop-color="var(--herb-dark)"/>
        <stop offset="0.55" stop-color="var(--herb-light)"/>
        <stop offset="1" stop-color="var(--paper)"/>
      </radialGradient>
    </defs>

    <!-- envelope die shape -->
    <path class="envelope-body" fill="var(--leaf)" d="
      M225 188 H547 L574 161 V143 Q574 119 598 119 H910 Q935 119 935 143 V161 L960 188
      H983 Q1003 190 1003 212 V673 Q1003 695 983 695 H960 L935 722 V741 Q935 765 910 765
      H598 Q574 765 574 741 V724 L547 697 H225 Q201 697 201 673 V212 Q201 188 225 188 Z"/>

    <!-- back panel frame -->
    <rect class="back-frame" x="260" y="254" width="291" height="377" fill="none" stroke="var(--ink)" stroke-width="0.8"/>

    <!-- brand seal circle -->
    <circle class="brand-seal" cx="406" cy="350" r="72" fill="var(--paper)" stroke="var(--ink)" stroke-width="3"/>

    <!-- social circles -->
    <g class="social-dots" fill="var(--paper)">
      <circle cx="368" cy="585" r="11"/>
      <circle cx="399" cy="585" r="11"/>
      <circle cx="430" cy="585" r="11"/>
    </g>

    <!-- flap glue strip -->
    <rect class="glue-strip" x="591" y="137" width="324" height="29" rx="8" fill="none" stroke="var(--ink)" stroke-width="0.8"/>

    <!-- fold lines -->
    <g class="fold-lines" fill="none" stroke="var(--ink)" stroke-width="0.8" stroke-dasharray="14 8">
      <path d="M594 181 H943 V704 H565 V181 H594"/>
    </g>

    <!-- front panel -->
    <path class="hero-band" fill="var(--leaf-deep)" d="M579 196 H927 V335 Q880 408 753 410 Q626 408 579 343 Z"/>
    <path class="hero-window" fill="url(#herbGlow)" role="img" aria-label="Photograph of a fresh bunch of curly parsley tied with twine" d="M579 196 H927 V335 Q870 400 753 400 Q636 400 579 330 Z"/>
    <rect class="front-frame" x="579" y="196" width="348" height="493" fill="none" stroke="var(--ink)" stroke-width="0.8"/>
  </svg>

  <div class="seal-name">TALL MEADOW<br>PANTRY</div>

  <p class="label back-text kicker">PREMIER QUALITY</p>
  <p class="label back-text product">PARSLEY SEED</p>
  <p class="label back-text website">www.tallmeadowpantry.example</p>
  <p class="label back-text handle">@tallmeadowpantry</p>

  <h1 class="label brand-title">TALL MEADOW<br>PANTRY</h1>

  <p class="label front-foot seed-name">Parsley SEED</p>
  <p class="label front-foot net-weight">Net wt. 100g</p>
</main>
</body>
</html>
```